Kunststoffverpackung für Falkor Snacks
Zielgruppe
Wir sind ein kleines Unternehmen, welches Bisonfleisch aus Nordamerika importiert und vertreibt. Unser neustes Produkt sind Falkor Snacks, deren Verpackung wir uns gerne designen lassen möchten.
Aufgabenstellung:
Design Entwurf für eine Kunststoffverpackung für Falkor Snacks (Trockenfleisch), von kanadischem Bison.
Preissegment: hochpreisig
Verkauf: Delikatessengeschäfte, hochpreisige Kaufhäuser (zb Lumhaus Berlin)
Design: edel, understatement, wenige ausgewählte Farben
Implizierte Message: hochwertiges, nachhaltiges Produkt für Feinschmecker und gesundheitsbewusste Sportler/Abenteurer.
USP: Jerky aus original kanadischem Bisonfleisch, artgerecht aufgezogen, ohne Medikamente, Wachstumshormone oder Futterzusätze
Besondere Produkteigenschaft: Kein Zucker, hoher Proteinanteil, hoher Eisenanteil, niedriger Cholesterinwert, kaum Fett, wenig Salz.
Aufgabenstellung
Zusätzliche Infos zu unserem Bisonfleisch findest du hier:
https://weidekorn-example.de/blogs/news/uber-uns-bisonfleisch-das-beste-fleisch-der-welt
https://weidekorn-example.de/blogs/news/bison-steak-guide
Zusätzliche Informationen zu Bisons findest du hier:
https://weidekorn-example.de/pages/bison-wiki
Auf der Rückseite bitte Platz lassen für folgende Grafiken/Informationen, daher bitte Platzhalter einfügen:
- Zutatenliste
- Nährwerttabelle
- Strichcode
- Recyclinglabel
Maße für die Verpackung sind:
170mm Länge
130mm Breite
Fotos wie die Verpackung auf keinen Fall aussehen sollen befinden sich mit dem Namen 'Dont' anbei. Verpackungen die uns vom Design gefallen befinden sich mit dem Namen 'Do' anbei.
Bei Rückfragen bitte mobil oder per mail wenden an:
Matthias Oldörp

```html
<!DOCTYPE html>
<html lang="de">
<head>
<meta charset="utf-8">
<title>Weidekorn – Jerky Verpackung</title>
<link rel="stylesheet" href="https://fonts.googleapis.com/css2?family=Antonio:wght@100;200&family=Cookie&family=Libre+Baskerville:wght@700&family=Rubik+Dirt&display=swap">
<style>
  :root {
    --paper: #e4dfd3;
    --paper-deep: #d3cdc0;
    --band: #1e1e1e;
    --ink: #333231;
    --ink-soft: #3b3b3b;
    --red: #a02a2b;
    --white: #ffffff;
  }
  * { margin: 0; padding: 0; box-sizing: border-box; }
  html, body { width: 918px; height: 1200px; overflow: hidden; }
  body { background: var(--paper); }
  ul { list-style: none; }

  .pack {
    position: relative;
    width: 918px;
    height: 1200px;
    overflow: hidden;
    background: radial-gradient(ellipse at 40% 60%, var(--paper) 0%, var(--paper-deep) 100%);
  }

  .top-band {
    position: absolute; left: 0; top: 0;
    width: 918px; height: 158px;
    background: var(--band);
  }
  .brand {
    position: absolute; left: 201px; top: 34px;
    width: 570px; height: 95px;
    background: #000;
    display: flex; align-items: center; justify-content: center; gap: 26px;
  }
  .brand-circle {
    width: 86px; height: 86px;
    border: 3px solid var(--white);
    border-radius: 50%;
  }
  .brand-name {
    font-family: "Libre Baskerville", serif;
    font-weight: 700;
    font-size: 52px;
    color: var(--white);
    letter-spacing: 1px;
  }

  .product-art {
    position: absolute; left: 250px; top: 470px;
    width: 668px; height: 720px;
    background: radial-gradient(ellipse at 55% 45%, #efece6 0%, #c9c5bd 70%, rgba(201,197,189,0) 100%);
  }

  .headline {
    position: absolute; left: 27px; top: 134px;
    font-family: "Rubik Dirt", sans-serif;
    font-weight: 400;
    font-size: 232px;
    line-height: 1;
    color: var(--ink);
    letter-spacing: -6px;
    white-space: nowrap;
    transform: scaleY(1.4);
    transform-origin: top left;
  }
  .subline {
    position: absolute; left: 34px; top: 421px;
    font-family: "Rubik Dirt", sans-serif;
    font-size: 42px;
    line-height: 1;
    color: var(--red);
    letter-spacing: 2.5px;
    white-space: nowrap;
  }
  .net-weight {
    position: absolute; left: 30px; top: 474px;
    font-family: "Antonio", sans-serif;
    font-weight: 100;
    font-size: 40px;
    line-height: 1;
    color: var(--ink);
    letter-spacing: 11px;
    white-space: nowrap;
  }
  .tagline {
    position: absolute; left: 32px; top: 516px;
    font-family: "Cookie", cursive;
    font-size: 92px;
    line-height: 1;
    color: var(--ink-soft);
    white-space: nowrap;
  }

  .benefits { position: absolute; left: 0; top: 0; width: 918px; height: 1200px; }
  .benefit {
    position: absolute; bottom: 8px;
    writing-mode: vertical-rl;
    transform: rotate(180deg);
    font-family: "Antonio", sans-serif;
    font-weight: 200;
    font-size: 23px;
    line-height: 1;
    color: var(--ink);
    white-space: nowrap;
  }
  .marker {
    position: absolute; top: 1124px;
    width: 18px; height: 18px;
    border-radius: 50%;
    background: var(--red);
    transform: translateX(-9px);
  }
</style>
</head>
<body>
<main class="pack">
  <header class="top-band">
    <div class="brand">
      <span class="brand-circle"></span>
      <span class="brand-name">WEIDEKORN</span>
    </div>
  </header>

  <div class="product-art" role="img" aria-label="Gestochene Illustration eines Bisons in Grautönen vor blassem Gräser- und Blattmuster"></div>

  <h1 class="headline">JERKY</h1>
  <p class="subline">ORIGINAL CANADIAN BISONFLEISCH</p>
  <p class="net-weight">NET WT. 2.25 OZ (64G)</p>
  <p class="tagline">Handcrafted</p>

  <ul class="benefits">
    <li class="marker" style="left:41px"></li>
    <li class="marker" style="left:108px"></li>
    <li class="marker" style="left:176px"></li>
    <li class="marker" style="left:244px"></li>
    <li class="marker" style="left:306px"></li>
    <li class="marker" style="left:374px"></li>
    <li class="marker" style="left:437px"></li>
    <li class="marker" style="left:499px"></li>
    <li class="marker" style="left:563px"></li>
    <li class="marker" style="left:741px"></li>
    <li class="marker" style="left:807px"></li>
    <li class="marker" style="left:875px"></li>

    <li class="benefit" style="left:60px">Artgerecht aufgezogen</li>
    <li class="benefit" style="left:125px">Ohne Medikamentenzugabe</li>
    <li class="benefit" style="left:191px">Ohne Zugabe von Wachstumshormonen</li>
    <li class="benefit" style="left:259px">Ohne Futterzusätze</li>
    <li class="benefit" style="left:322px">Niedrige Cholesterinwerte</li>
    <li class="benefit" style="left:387px">Hoher Proteinanteil</li>
    <li class="benefit" style="left:450px">Hoher Eisenanteil</li>
    <li class="benefit" style="left:513px">Kein Zucker</li>
    <li class="benefit" style="left:754px">Wenig Fett</li>
    <li class="benefit" style="left:822px">Wenig Salz</li>
  </ul>
</main>
</body>
</html>
```